O Balcão KEZ - costumer paper bag

We need a new design for the paper bags of our stores located in Portugal (Funchal and Lisboa).
The design must use logo colors. The final design should comunicate top fashion image, glamour and exclusivity.
We are a gowns and accessories speciality store with 4 fisical locations and online at www.obalcao.pt

Target Market(s)

Mass market, up scale consumers

Industry/Entity Type

Kez

Requirements
Must have
• . keep diamonds in logo of the letters KEZ
• . simple design
• - work only with the colors black, white, silver
• - modern
Nice to have
• elegante and simple design
Should not have
• differente colors other of the mentioned above
• complicated desing

```html
<!DOCTYPE html>
<html lang="pt">
<head>
<meta charset="utf-8">
<title>O Balcão KEZ — Saco de loja</title>
<link rel="stylesheet" href="https://fonts.googleapis.com/css2?family=Questrial&family=Open+Sans:wght@400&display=swap">
<style>
  :root {
    --bag-black: #1c1a1b;
    --stripe-white: #ffffff;
    --stripe-black: #121011;
    --ornament-grey: #2a2829;
    --silver: #c9c9cb;
    --text-white: #ffffff;
  }
  html, body {
    margin: 0;
    padding: 0;
    width: 900px;
    height: 1200px;
    overflow: hidden;
    background: var(--bag-black);
  }
  .bag {
    position: relative;
    width: 900px;
    height: 1200px;
    background: var(--bag-black);
    overflow: hidden;
  }
  .side-ornament {
    position: absolute;
    top: 0;
    width: 105px;
    height: 1200px;
    background: linear-gradient(180deg, var(--ornament-grey), var(--bag-black) 50%, var(--ornament-grey));
  }
  .side-ornament--left { left: 0; }
  .side-ornament--right { right: 0; width: 110px; }
  .stripe-panel {
    position: absolute;
    left: 105px;
    width: 685px;
    background: repeating-linear-gradient(90deg,
      var(--stripe-white) 0 9px,
      var(--stripe-black) 9px 18px);
  }
  .stripe-panel--top { top: 0; height: 515px; }
  .stripe-panel--bottom { top: 685px; height: 515px; }
  .handle-cutout {
    position: absolute;
    left: 225px;
    top: 55px;
    width: 450px;
    height: 120px;
    border-radius: 26px;
    background: var(--stripe-black);
  }
  .brand-band {
    position: absolute;
    left: 0;
    top: 515px;
    width: 900px;
    height: 170px;
    background: var(--bag-black);
  }
  .brand-mark {
    position: absolute;
    left: 62px;
    top: 530px;
    width: 62px;
    height: 62px;
    background: var(--text-white);
  }
  .brand-name {
    position: absolute;
    left: 172px;
    top: 540px;
    margin: 0;
    font-family: "Questrial", "Century Gothic", sans-serif;
    font-weight: 400;
    font-size: 82px;
    line-height: 1;
    color: var(--text-white);
    letter-spacing: -1px;
  }
  .brand-tier {
    position: absolute;
    left: 625px;
    top: 538px;
    margin: 0;
    font-family: "Questrial", "Century Gothic", sans-serif;
    font-weight: 400;
    font-size: 92px;
    line-height: 1;
    color: var(--silver);
    letter-spacing: 2px;
  }
  .brand-url {
    position: absolute;
    left: 0;
    top: 652px;
    width: 900px;
    margin: 0;
    text-align: center;
    font-family: "Open Sans", Arial, sans-serif;
    font-size: 22px;
    color: var(--text-white);
    letter-spacing: 0.5px;
  }
</style>
</head>
<body>
  <div class="bag">
    <div class="side-ornament side-ornament--left" role="img" aria-label="Grey floral swirl ornaments on black"></div>
    <div class="side-ornament side-ornament--right" role="img" aria-label="Grey floral swirl ornaments on black"></div>

    <div class="stripe-panel stripe-panel--top" role="img" aria-label="Black and white vertical stripes with grey swirl ornaments"></div>
    <div class="handle-cutout"></div>

    <div class="brand-band"></div>
    <div class="brand-mark"></div>
    <p class="brand-name">O Balcão</p>
    <p class="brand-tier">KEZ</p>
    <p class="brand-url">www.obalcao.pt</p>

    <div class="stripe-panel stripe-panel--bottom" role="img" aria-label="Black and white vertical stripes with grey swirl ornaments"></div>
  </div>
</body>
</html>
```